QM_radiance is a new upcoming amazing brand for modesty women , which started in 2016.

Design a page with all products and stating the title of the collection and style of the products and pricing.
Will need to create a column of upcoming events as well for customer to keep updated of our sales or flea

Target Market(s)

Hijabista, modesttrend

Number of Pages Required

5+ page

Requirements
Nice to have
• About Us
• Our brand represents classy and elegance yet it is comfortable and conservative to be worn everyday.
• Designs, and colours of fabrics chiffon , silk crepe and sateen silks and viscose cotton are exclusively chosen by QMradiance, imported from mainly high quality materials and sent for self manufactured.
• InsyaAllah#QMradiance

```html
<!DOCTYPE html>
<html lang="en">
<head>
<meta charset="utf-8">
<title>QM Radiance — Modest Wear</title>
<link href="https://fonts.googleapis.com/css2?family=Fira+Sans:wght@300;400;500&display=swap" rel="stylesheet">
<style>
:root{
  --ink:#2b2b2b;
  --muted:#666;
  --soft:#8a8a8a;
  --pink:#dc3d66;
  --band:#f5f5f5;
  --line:#e3e3e3;
  --white:#fff;
  --black:#0c0c0c;
}
*{box-sizing:border-box;margin:0;padding:0}
html,body{width:1200px;height:2390px;overflow:hidden;background:var(--white)}
body{position:relative;font-family:"Fira Sans",sans-serif;color:var(--ink);font-weight:300}
.abs{position:absolute}
a{color:inherit;text-decoration:none}

/* header */
.account-links{left:73px;top:59px;font-size:13px;letter-spacing:.5px;color:var(--muted)}
.account-links span{margin:0 8px}
.brand{left:480px;top:34px;width:240px;text-align:center}
.brand-mark{display:block;width:34px;height:34px;margin:0 auto 10px;border:2px solid var(--black)}
.brand-name{font-size:26px;font-weight:400;color:var(--black);letter-spacing:.5px}
.bag{right:70px;top:58px;font-size:13px;color:var(--muted);display:flex;align-items:center;gap:6px}
.main-nav{left:0;top:150px;width:1200px;font-size:13px;letter-spacing:1px;color:var(--muted)}
.main-nav a,.main-nav i{position:absolute;font-style:normal;transform:translateX(-50%);white-space:nowrap}

/* hero */
.hero{left:0;top:183px;width:1200px;height:463px;background:var(--band)}
.hero-title{left:73px;top:282px;font-size:33px;font-weight:300;color:var(--ink)}
.hero-title b{color:var(--pink);font-weight:500}
.hero-text{left:73px;top:337px;width:420px;font-size:14px;line-height:22px;color:var(--muted)}
.btn-outline{left:73px;top:437px;width:98px;height:35px;border:1px solid var(--ink);font-size:12px;display:flex;align-items:center;justify-content:center;letter-spacing:.5px;font-weight:400}
.dots{left:73px;top:595px;display:flex;gap:3px}
.dots span{width:11px;height:11px;border-radius:50%;background:#ddd}
.dots span:first-child{background:#bbb}
.hero-visual{left:610px;top:239px;width:514px;height:343px;background:linear-gradient(90deg,#b9b3c9 0 22%,#f3aeb0 22% 46%,#3a3f35 46% 72%,#2f3327 72%);transform:skewY(-3deg)}

/* collections */
.collection{top:673px;width:333px;height:475px;overflow:hidden}
.collection .photo{position:absolute;inset:0}
.collection .caption{position:absolute;left:0;top:371px;width:100%;height:91px;background:rgba(255,255,255,.72);text-align:center}
.collection h3{font-size:28px;font-weight:300;margin-top:16px;color:var(--ink)}
.tag{display:inline-block;margin-top:6px;width:121px;height:26px;line-height:26px;background:var(--pink);color:var(--white);font-size:12px;font-weight:400;clip-path:polygon(0 0,100% 0,94% 50%,100% 100%,0 100%,6% 50%)}

/* featured */
.section-rule{top:1206px;height:14px;background:repeating-linear-gradient(135deg,#eee 0 2px,#f8f8f8 2px 5px)}
.section-title{left:0;top:1202px;width:1200px;text-align:center;font-size:16px;font-weight:400;letter-spacing:.5px}
.product{top:1278px;width:244px;text-align:center}
.product .photo{height:372px}
.product .badge{position:absolute;left:103px;top:353px}
.product h4{margin-top:36px;font-size:16px;font-weight:300;color:var(--ink)}
.product .price{margin-top:10px;font-size:16px;color:var(--pink);font-weight:400}

/* about & events */
.block-title{top:1824px;font-size:18px;font-weight:400;letter-spacing:.5px}
.about-text{left:73px;top:1860px;width:490px;font-size:14px;line-height:23.3px;color:var(--muted)}
.event{top:1870px;width:243px}
.event .photo{height:146px}
.event .meta{margin-top:14px;font-size:11px;color:var(--soft)}
.event p{margin-top:6px;font-size:14px;line-height:21px;color:var(--muted)}

/* footer */
.footer{left:0;top:2164px;width:1200px;height:226px;background:var(--band);border-top:8px solid #ececec}
.news-title{left:73px;top:2203px;font-size:15px;font-weight:400;display:flex;align-items:center;gap:8px}
.news-input{left:73px;top:2243px;width:201px;height:32px;border:1px solid #ccc;background:var(--white);font-size:13px;color:var(--soft);padding:0 8px;line-height:30px}
.news-btn{left:285px;top:2243px;width:123px;height:32px;background:var(--black);color:var(--white);font-size:12.5px;font-weight:400;text-align:center;line-height:32px}
.social{left:73px;top:2305px;display:flex;gap:6px}
.social span{width:32px;height:32px;border-radius:50%;border:2px solid #2e6fb3;background:var(--white)}
.copyright{left:73px;top:2348px;font-size:12px;color:var(--muted)}
.link-col{top:2206px;font-size:12.5px;color:var(--muted)}
.link-col h5{font-size:12.5px;font-weight:500;color:var(--ink);letter-spacing:.5px;margin-bottom:9px}
.link-col li{list-style:none;line-height:26px}
</style>
</head>
<body>

<header>
  <div class="abs account-links"><a href="#">SIGN IN</a><span>|</span><a href="#">REGISTER</a></div>
  <div class="abs brand"><span class="brand-mark"></span><span class="brand-name">QM Radiance</span></div>
  <div class="abs bag">
    <svg width="16" height="14" viewBox="0 0 16 14"><path d="M1 5h14l-2 8H3z M4 5l4-4 4 4" fill="none" stroke="#666" stroke-width="1.4"/></svg>
    SHOPPING BAG (0)
  </div>
  <nav class="abs main-nav">
    <a style="left:204px">HOME</a><i style="left:260px">/ /</i>
    <a style="left:327px">PRODUCTS</a><i style="left:396px">/ /</i>
    <a style="left:488px">OUR COLLECTION</a><i style="left:580px">/ /</i>
    <a style="left:676px">UPCOMING EVENTS</a><i style="left:773px">/ /</i>
    <a style="left:853px">ABOUT US</a><i style="left:911px">/ /</i>
    <a style="left:980px">CONATC US</a>
  </nav>
</header>

<section>
  <div class="abs hero"></div>
  <h1 class="abs hero-title">New Arrival Upcoming <b>2016</b></h1>
  <p class="abs hero-text">Lorem ipsum dolor sit amet, consectetuer adipiscing elit, sed diam nonummy nibh euismod tincidunt ut laoreet dolore magna aliquam erat volutpat.</p>
  <a class="abs btn-outline">SHOP NOW</a>
  <div class="abs dots"><span></span><span></span><span></span><span></span><span></span></div>
  <div class="abs hero-visual" role="img" aria-label="Four folded printed scarves: feather print, pink dots, leaf print and green pattern"></div>
</section>

<section>
  <div class="abs collection" style="left:73px">
    <div class="photo" role="img" aria-label="Model wearing a magenta chiffon hijab" style="background:linear-gradient(180deg,#c7cbd4,#c03a92 45%,#e8e8ec 80%)"></div>
    <div class="caption"><h3>Sparkle</h3><span class="tag">COLLECTION</span></div>
  </div>
  <div class="abs collection" style="left:434px">
    <div class="photo" role="img" aria-label="Model wearing a red hijab with flower beads" style="background:linear-gradient(180deg,#c7cbd4,#b51c3c 45%,#e8e8ec 80%)"></div>
    <div class="caption"><h3>Flower Beads</h3><span class="tag">COLLECTION</span></div>
  </div>
  <div class="abs collection" style="left:794px">
    <div class="photo" role="img" aria-label="Model wearing a green crystal-embellished hijab" style="background:linear-gradient(180deg,#c7cbd4,#1c5a3a 45%,#e8e8ec 80%)"></div>
    <div class="caption"><h3>Crystalline</h3><span class="tag">COLLECTION</span></div>
  </div>
</section>

<section>
  <div class="abs section-rule" style="left:73px;width:425px"></div>
  <div class="abs section-rule" style="left:703px;width:424px"></div>
  <h2 class="abs section-title">FEATURED PRODUCTS</h2>

  <div class="abs product" style="left:73px">
    <div class="photo" role="img" aria-label="Navy hijab on model" style="background:linear-gradient(180deg,#e9e9ef,#1f2233 40%,#1a1a1a)"></div>
    <svg class="badge" width="38" height="40" viewBox="0 0 38 40"><polygon points="19,1 37,10.5 37,29.5 19,39 1,29.5 1,10.5" fill="var(--pink)"/><path d="M12 17h14l-2 9h-10z M15 17l4-4 4 4" fill="none" stroke="#fff" stroke-width="1.6"/></svg>
    <h4>Product Name</h4><div class="price">$30.00</div>
  </div>
  <div class="abs product" style="left:343px">
    <div class="photo" role="img" aria-label="Peach floral hijab on model" style="background:linear-gradient(180deg,#ececf0,#f6c7ad 40%,#1c1c1c 85%)"></div>
    <svg class="badge" width="38" height="40" viewBox="0 0 38 40"><polygon points="19,1 37,10.5 37,29.5 19,39 1,29.5 1,10.5" fill="var(--pink)"/><path d="M12 17h14l-2 9h-10z M15 17l4-4 4 4" fill="none" stroke="#fff" stroke-width="1.6"/></svg>
    <h4>Product Name</h4><div class="price">$30.00</div>
  </div>
  <div class="abs product" style="left:614px">
    <div class="photo" role="img" aria-label="Cream butterfly print hijab on model" style="background:linear-gradient(180deg,#e6e6ec,#ece3d6 40%,#1c1c1c 85%)"></div>
    <svg class="badge" width="38" height="40" viewBox="0 0 38 40"><polygon points="19,1 37,10.5 37,29.5 19,39 1,29.5 1,10.5" fill="var(--pink)"/><path d="M12 17h14l-2 9h-10z M15 17l4-4 4 4" fill="none" stroke="#fff" stroke-width="1.6"/></svg>
    <h4>Product Name</h4><div class="price">$30.00</div>
  </div>
  <div class="abs product" style="left:883px">
    <div class="photo" role="img" aria-label="Grey hijab on model" style="background:linear-gradient(180deg,#e6e6ec,#7a7a7c 40%,#1c1c1c 90%)"></div>
    <svg class="badge" width="38" height="40" viewBox="0 0 38 40"><polygon points="19,1 37,10.5 37,29.5 19,39 1,29.5 1,10.5" fill="var(--pink)"/><path d="M12 17h14l-2 9h-10z M15 17l4-4 4 4" fill="none" stroke="#fff" stroke-width="1.6"/></svg>
    <h4>Product Name</h4><div class="price">$30.00</div>
  </div>
</section>

<section>
  <h2 class="abs block-title" style="left:73px">ABOUT US</h2>
  <p class="abs about-text">Lorem ipsum dolor sit amet, consectetuer adipiscing elit, sed diam nonummy nibh euismod tincidunt ut laoreet dolore magna aliquam erat volutpat. Ut wisi enim ad minim veniam, quis nostrud exerci tation ullamcorper suscipit lobortis nisl ut aliquip ex ea commodo consequat. Duis autem vel eum iriure dolor in hendrerit in vulputate velit esse molestie consequat, enim ad minim veniam, quis nostrud exerci tation ullamcorper suscipit lobortis nisl ut aliquip ex ea commodo consequat. vel illum dolore eu feugiat nulla facilisis at vero eros et accumsan et iusto odio dignissim qui blandit praesent luptatum zzril delenit augue duis dolore te feugait nulla facilisi</p>

  <h2 class="abs block-title" style="left:614px">UPCOMING EVENTS</h2>
  <div class="abs event" style="left:614px">
    <div class="photo" role="img" aria-label="Sequinned evening dress" style="background:linear-gradient(90deg,#3a3330,#c9b4a6 50%,#6b5a52)"></div>
    <div class="meta">25 Jun 2016 | London</div>
    <p>Lorem ipsum dolor sit amet, consecte adipiscing elit...</p>
  </div>
  <div class="abs event" style="left:885px">
    <div class="photo" role="img" aria-label="Red lace dress with white hijab" style="background:linear-gradient(90deg,#e8e8ea,#d8243a 50%,#d4d6da)"></div>
    <div class="meta">25 Jun 2016 | London</div>
    <p>Lorem ipsum dolor sit amet, consecte adipiscing elit...</p>
  </div>
</section>

<footer>
  <div class="abs footer"></div>
  <h3 class="abs news-title">
    <svg width="20" height="16" viewBox="0 0 20 16"><path d="M1 6l9-5 9 5v9H1z" fill="#222"/><path d="M1 6l9 6 9-6" fill="none" stroke="#fff" stroke-width="1.2"/></svg>
    SUBSCRIBE TO OUR NEWSLETTER!
  </h3>
  <div class="abs news-input">Email Address</div>
  <div class="abs news-btn">SUBSCRIBE NOW!</div>
  <div class="abs social"><span></span><span></span><span></span><span></span><span></span></div>
  <p class="abs copyright">©2016 QM Radiance. All Rights Resreved.</p>

  <div class="abs link-col" style="left:524px"><h5>QUICK LINK</h5><ul><li>Home</li><li>Products</li><li>Our Collection</li><li>Upcoming Events</li><li>Conatc Us</li></ul></div>
  <div class="abs link-col" style="left:748px"><h5>CUSTOMER CARE</h5><ul><li>Contact Us</li><li>Returns</li><li>Site Map</li><li>Free Shipping</li></ul></div>
  <div class="abs link-col" style="left:976px"><h5>MY ACCOUNT</h5><ul><li>My Account</li><li>Order History</li><li>Wish List</li><li>Newsletter</li></ul></div>
</footer>

</body>
</html>
```